New Digital Marketing Company Needs Web Design

Introduction

Brightcrest gives advice to small businesses about their websites and digital marketing strategies and builds working relationships with clients to understand their business and maximise its online presence.

Brightcrest offers services to support its clients needs such as: website auditing & search engine optimisation (SEO), Quorvo Promoline, Chatterlane advertising, newsletter development & management, online performance reporting, email setup & management, website hosting, maintenance & backup, web development, web updates & web design.

Design Specification

The site should have a clean & professional look and use the colour scheme from the logo (attached below).

The design should consist of 2 templates; The homepage & content page.

Homepage Design

The homepage should have a header with logo, contact number and email and menu. Followed underneath by a slider and then individual blocks for key services. Under the key services should be a testimonial block with 3 testimonials. Finally the footer with company details, menu links and location map.

Header Info:

Contact number: 01632 960481
Email: info@brightcrest-demo.co.uk

Menu: Home Services About Contact

Slider Design:

The slider should be full page and show an image with text.

Key Services:

The key services should have a relevant icon and brief description.

The key services are:

Digital Marketing

Website Hosting & Management

Website Health Check (SEO)

Website Updating & Development

Newsletter Management

Email Management

Note: Lorem Ipsum can be used for brief description...

Testimonials:

There should be 3 testimonials side by side and they should include a headshot image of the person giving the testimonial.

Note: Lorem Ipsum and sample images can be used for testimonials...

Footer:

The footer should have 3 sections:

Menu links:

Digital Marketing About
Quorvo Promoline Contact
Chatterlane Advertising Privacy Policy
Search Engine Optimisation (SEO) Terms & Conditions
Website Hosting FAQ
Newsletter Management

Company Information:

BrightCrest
14 Marlow Close
Bracknell
Berskhire
ZZ9 4QT
Tel: 01632 960481

Chatterlane icon - Pipwave icon - Careernest icon

Location

Quorvo map

Footer Bottom:

Copyright message.

Content Design

The content design should have the common header and footer.

Each content page should have a banner for image with text description (page title).

The content page should have area for text description and area for a video display if available.

There should be a right column (possibly) for modules (latest blog, latest Chatterlane feeds, testimonial)

Project Deadline Extended
Reason: I have had to extend the deadline as could not review while on vacation and need to feedback to some designers for content page design. Many thanks for your understanding.

Target Market(s)

Industry/Entity Type

Digital

Number of Pages Required

2 page

Requirements
Must have
• The site should have a clean & professional look and use the colour scheme from the logo (attached below).
• The design should consist of 2 templates; The homepage & content page.

```html
<!DOCTYPE html>
<html lang="en">
<head>
<meta charset="utf-8">
<title>BrightCrest – Home</title>
<link href="https://fonts.googleapis.com/css2?family=Open+Sans:wght@400;600;700&family=Lato:wght@400;700&display=swap" rel="stylesheet">
<style>
:root{
  --plum:#74285a;
  --plum-dark:#651d4d;
  --ink:#2b2b2b;
  --grey-text:#666;
  --panel:#ebebeb;
  --cell:#f2f2f2;
  --footer:#0e0e0e;
  --white:#fff;
}
*{margin:0;padding:0;box-sizing:border-box}
html,body{width:888px;height:1200px;overflow:hidden;background:var(--white)}
body{position:relative;font-family:'Lato',sans-serif;color:var(--ink)}
.abs{position:absolute}

/* header */
.site-header{position:absolute;left:0;top:0;width:888px;height:70px;border-top:2px solid var(--plum);background:linear-gradient(#fff,#f6f6f6)}
.brand{left:86px;top:16px;display:flex;align-items:center;gap:6px}
.brand-dot{width:26px;height:26px;border-radius:50%;background:var(--plum)}
.brand-name{font-family:'Open Sans',sans-serif;font-weight:700;font-size:24px;color:var(--plum);line-height:1}
.brand-tag{left:122px;top:45px;font-family:'Open Sans',sans-serif;font-size:7.5px;letter-spacing:1.6px;color:#444}
.contact-line{top:14px;font-size:10px;color:#333;display:flex;align-items:center;gap:8px}
.contact-line svg{width:10px;height:10px}
.main-nav{right:88px;top:47px;display:flex;font-size:8.5px;color:#444;letter-spacing:.3px}
.main-nav span{padding:0 17px;border-left:1px dotted #bbb;line-height:12px}
.main-nav span:first-child{border:0;color:var(--plum);font-weight:700}
.main-nav span:last-child{padding-right:0}

/* hero */
.hero{left:0;top:70px;width:888px;height:279px;background:var(--plum)}
.hero-title{left:84px;top:82px;font-family:'Open Sans',sans-serif;font-weight:700;font-size:25px;color:#fff;letter-spacing:.3px}
.hero-sub{left:86px;top:117px;width:300px;font-size:12px;line-height:15px;color:#fff}
.btn{top:158px;height:28px;font-size:8.5px;display:flex;align-items:center;justify-content:center;letter-spacing:.3px}
.btn-dark{left:88px;width:94px;background:#161616;color:#fff}
.btn-light{left:192px;width:95px;background:#fff;color:#222}
.hero-art{left:468px;top:38px;width:334px;height:192px;border-radius:6px;background:linear-gradient(135deg,#e9eef2,#9fc9dc 55%,#f3b33d)}
.slide-dots{left:425px;top:244px;display:flex;gap:6px;align-items:center}
.slide-dots i{width:7px;height:7px;border-radius:50%;background:#fff}
.slide-dots i.on{width:10px;height:10px;background:transparent;border:1.5px solid #fff}

/* services */
.services-intro{left:0;top:349px;width:263px;height:239px;background:var(--panel)}
.services-intro::after{content:"";position:absolute;right:-8px;top:110px;border-left:8px solid var(--panel);border-top:8px solid transparent;border-bottom:8px solid transparent}
.intro-icon{left:140px;top:33px;width:60px;height:60px;border-radius:50%;background:#fff;display:flex;align-items:center;justify-content:center}
.intro-title{left:0;top:108px;width:340px;text-align:center;font-family:'Open Sans',sans-serif;font-weight:700;font-size:17px;color:#222}
.intro-title b{color:var(--plum)}
.intro-text{left:80px;top:134px;width:180px;text-align:center;font-size:8.5px;line-height:12px;color:var(--grey-text)}
.btn-view{left:126px;top:171px;width:88px;height:27px;background:var(--plum);color:#fff;font-size:8.5px;display:flex;align-items:center;justify-content:center}
.service-cell{background:var(--cell);height:118px}
.service-cell .ico{position:absolute;left:50%;top:18px;width:56px;height:56px;margin-left:-28px;border-radius:50%;background:#e3e3e3;display:flex;align-items:center;justify-content:center}
.service-cell .ico.active{background:var(--plum)}
.service-cell .label{position:absolute;left:0;right:0;top:86px;text-align:center;font-family:'Open Sans',sans-serif;font-size:11px;color:#333}

/* testimonials */
.section-title{left:0;top:618px;width:888px;text-align:center;font-family:'Open Sans',sans-serif;font-weight:700;font-size:20px;color:#222}
.section-title b{color:var(--plum)}
.divider{left:324px;top:657px;width:240px;height:1px;background:#ddd}
.divider-dot{left:439px;top:650px;width:10px;height:12px;border-radius:50%;border:1.5px solid #ddd;background:#fff}
.lead{left:0;top:676px;width:888px;text-align:center;font-size:10px;line-height:16px;color:#444}
.avatar{top:722px;width:60px;height:60px;border-radius:50%;border:2px solid #bbb;background:linear-gradient(#c9c9c9,#8a8a8a)}
.avatar.first{border-color:var(--plum)}
.client-name{top:794px;width:226px;text-align:center;font-family:'Open Sans',sans-serif;font-weight:600;font-size:10.5px;color:#222}
.client-handle{top:813px;width:226px;text-align:center;font-size:9px;color:var(--plum);font-weight:700}
.quote-box{top:841px;width:226px;height:89px;border:1px solid #ddd;background:#fff;padding:13px 16px 0}
.quote-box.first{border-color:var(--plum);border-bottom-width:2px}
.quote-box::before{content:"";position:absolute;left:106px;top:-7px;width:12px;height:12px;background:#fff;border-left:1px solid #ddd;border-top:1px solid #ddd;transform:rotate(45deg)}
.quote-box.first::before{border-color:var(--plum)}
.quote-box p{font-size:9.5px;line-height:15.5px;color:#333}
.quote-box .date{position:absolute;left:16px;top:75px;font-size:7.5px;color:#555;letter-spacing:.2px}
.carousel-arrow{top:866px;width:22px;height:44px}

/* footer */
.site-footer{left:0;top:965px;width:888px;height:201px;background:var(--footer);color:#fff}
.foot-head{top:25px;font-family:'Open Sans',sans-serif;font-weight:400;font-size:14px;color:#fff}
.foot-links{left:85px;top:55px;font-size:8.5px;line-height:16px;list-style:none;color:#e6e6e6}
.foot-links li{padding-left:12px;position:relative}
.foot-links li.arrow::before{content:"›";position:absolute;left:0;top:0;color:#ccc}
.foot-contact{font-size:8.5px;color:#ccc;line-height:13px}
.foot-contact strong{color:#fff;font-weight:400}
.map-block{left:479px;top:33px;width:287px;height:110px;border-radius:3px;background:linear-gradient(120deg,#b9d6ec 0%,#e9e5dc 35%,#cfe3b5 70%,#e9e5dc 100%)}
.view-map{left:481px;top:152px;font-size:8.5px;color:#aaa}
.bottom-bar{left:0;top:1166px;width:888px;height:34px;background:var(--plum-dark);color:#fff;font-size:8.5px}
.social{width:20px;height:20px;border-radius:50%;background:#fff;top:7px}
</style>
</head>
<body>

<header class="site-header">
  <div class="abs brand"><span class="brand-dot"></span><span class="brand-name">BrightCrest</span></div>
  <div class="abs brand-tag">GROWING YOUR ONLINE REACH</div>
  <div class="abs contact-line" style="left:500px">
    <svg viewBox="0 0 10 10"><path d="M2 0.5l2 2-1 1.2c.6 1.3 1.7 2.4 3 3l1.2-1 2 2-1.3 1.6C4 9 1 6 0.6 1.8z" fill="var(--plum)"/></svg>
    <span>Call Us : 01632 960481</span>
  </div>
  <div class="abs contact-line" style="left:643px">
    <svg viewBox="0 0 10 10"><rect x="0.5" y="2" width="9" height="6.5" fill="var(--plum)"/><path d="M0.5 2l4.5 3.5L9.5 2" stroke="#fff" fill="none" stroke-width="0.8"/></svg>
    <span>Email: info@brightcrest-demo.co.uk</span>
  </div>
  <nav class="abs main-nav"><span>HOME</span><span>ABOUT US</span><span>SERVICES</span><span>CONTACT US</span></nav>
</header>

<section class="abs hero">
  <h1 class="abs hero-title">WEB DEVELOPMENT</h1>
  <p class="abs hero-sub">Lorem Ipsum is simply dummy text of the printing and typesetting industry.</p>
  <div class="abs btn btn-dark">LEARN MORE</div>
  <div class="abs btn btn-light">GET A QUOTE</div>
  <div class="abs hero-art" role="img" aria-label="Illustration of a desktop monitor, phone and web layout under construction with a crane and ladder"></div>
  <svg class="abs" style="left:36px;top:118px" width="16" height="32" viewBox="0 0 16 32"><path d="M14 2L2 16l12 14" stroke="#fff" stroke-width="1.5" fill="none"/></svg>
  <svg class="abs" style="left:836px;top:118px" width="16" height="32" viewBox="0 0 16 32"><path d="M2 2l12 14L2 30" stroke="#fff" stroke-width="1.5" fill="none"/></svg>
  <div class="abs slide-dots"><i></i><i class="on"></i><i></i></div>
</section>

<section>
  <div class="abs services-intro">
    <div class="abs intro-icon">
      <svg width="34" height="40" viewBox="0 0 34 40"><circle cx="16" cy="15" r="11" fill="none" stroke="#222" stroke-width="3"/><path d="M16 15V6a9 9 0 0 1 9 9z" fill="var(--plum)"/><rect x="14.5" y="26" width="3" height="13" fill="#222"/></svg>
    </div>
    <h2 class="abs intro-title">OUR <b>SERVICES</b></h2>
    <p class="abs intro-text">Lorem Ipsum is simply dummy text of the printing and typesetting industry.</p>
    <div class="abs btn-view">VIEW ALL</div>
  </div>

  <div class="abs service-cell" style="left:266px;top:349px;width:190px">
    <div class="ico"><svg width="24" height="24" viewBox="0 0 24 24"><circle cx="9" cy="9" r="6" fill="none" stroke="var(--plum)" stroke-width="2.5"/><path d="M13.5 13.5L21 21" stroke="var(--plum)" stroke-width="3"/></svg></div>
    <div class="label">Website Auditing &amp; (SEO)</div>
  </div>
  <div class="abs service-cell" style="left:458px;top:349px;width:189px">
    <div class="ico active"><svg width="24" height="22" viewBox="0 0 24 22"><rect x="3" y="10" width="4" height="10" fill="#fff"/><rect x="10" y="6" width="4" height="14" fill="#fff"/><rect x="17" y="9" width="4" height="11" fill="#fff"/><path d="M2 8l7-5 5 4 8-6" stroke="#fff" stroke-width="1.6" fill="none"/></svg></div>
    <div class="label">Quorvo Promoline</div>
  </div>
  <div class="abs service-cell" style="left:650px;top:349px;width:238px">
    <div class="ico"><svg width="24" height="24" viewBox="0 0 24 24"><ellipse cx="10" cy="5" rx="7" ry="3" fill="var(--plum)"/><path d="M3 5v11c0 1.7 3.1 3 7 3V5z" fill="var(--plum)"/><circle cx="17" cy="16" r="5" fill="none" stroke="var(--plum)" stroke-width="2"/></svg></div>
    <div class="label">Maintenance &amp; Backup</div>
  </div>
  <div class="abs service-cell" style="left:266px;top:470px;width:190px">
    <div class="ico"><svg width="24" height="24" viewBox="0 0 24 24"><circle cx="12" cy="12" r="10" fill="none" stroke="var(--plum)" stroke-width="2"/><path d="M2 12h20M12 2c4 4 4 16 0 20M12 2c-4 4-4 16 0 20" stroke="var(--plum)" stroke-width="1.5" fill="none"/></svg></div>
    <div class="label">Website Hosting</div>
  </div>
  <div class="abs service-cell" style="left:458px;top:470px;width:189px">
    <div class="ico"><svg width="26" height="22" viewBox="0 0 26 22"><rect x="1" y="2" width="20" height="15" fill="none" stroke="var(--plum)" stroke-width="1.6"/><rect x="5" y="10" width="2.5" height="5" fill="var(--plum)"/><rect x="9" y="7" width="2.5" height="8" fill="var(--plum)"/><rect x="13" y="9" width="2.5" height="6" fill="var(--plum)"/><circle cx="20" cy="5" r="4.5" fill="var(--plum)"/><path d="M0 19h24" stroke="var(--plum)" stroke-width="1.6"/></svg></div>
    <div class="label">Online Performance Reporting</div>
  </div>
  <div class="abs service-cell" style="left:650px;top:470px;width:238px">
    <div class="ico"><svg width="26" height="24" viewBox="0 0 26 24"><circle cx="9" cy="13" r="6" fill="none" stroke="var(--plum)" stroke-width="3.5" stroke-dasharray="3 2"/><circle cx="9" cy="13" r="2" fill="var(--plum)"/><path d="M12 14L23 3l2 2-11 11-3 1z" fill="var(--plum)"/></svg></div>
    <div class="label">Web Development</div>
  </div>
</section>

<section>
  <h2 class="abs section-title">CLIENTS <b>TESTIMONIALS</b></h2>
  <div class="abs divider"></div>
  <div class="abs divider-dot"></div>
  <p class="abs lead">It is a long established fact that a reader will be distracted by the readable content of a page when looking at its layout.<br>The point of using Lorem Ipsum is that it haa.</p>

  <svg class="abs carousel-arrow" style="left:47px" viewBox="0 0 22 44"><path d="M20 2L2 22l18 20" stroke="#ddd" stroke-width="1.5" fill="none"/></svg>
  <svg class="abs carousel-arrow" style="left:819px" viewBox="0 0 22 44"><path d="M2 2l18 20L2 42" stroke="#ddd" stroke-width="1.5" fill="none"/></svg>

  <div class="abs avatar first" style="left:169px" role="img" aria-label="Headshot of client Tavin Morrell"></div>
  <div class="abs client-name" style="left:86px">Mr. Tavin Morrell</div>
  <div class="abs client-handle" style="left:86px">@tmorrell</div>
  <div class="abs quote-box first" style="left:86px"><p>Ut wisi enim ad minim veniam, quisl mor nostrni exerci tation ullamcorper suskcipit no lobortis norl nislk ut aliquip.</p><span class="date">4:04PM - MAY, 2016</span></div>

  <div class="abs avatar" style="left:413px" role="img" aria-label="Headshot of client Lessa Varnik"></div>
  <div class="abs client-name" style="left:331px">Miss Lessa Varnik</div>
  <div class="abs client-handle" style="left:331px">@lvarnik</div>
  <div class="abs quote-box" style="left:331px"><p><span style="color:#ccc;font-size:14px">“</span> Ut wisi enim ad minim veniam, quisl mor nostrni exerci tation ullamcorper suskcipit no lobortis norl nislk ut aliquip.</p><span class="date">4:04PM - MAY, 2016</span></div>

  <div class="abs avatar" style="left:658px" role="img" aria-label="Headshot of client Orrin Bastell"></div>
  <div class="abs client-name" style="left:575px">Mr. Orrin Bastell</div>
  <div class="abs client-handle" style="left:575px">@obastell</div>
  <div class="abs quote-box" style="left:575px"><p><span style="color:#ccc;font-size:14px">“</span> Ut wisi enim ad minim veniam, quisl mor nostrni exerci tation ullamcorper suskcipit no lobortis norl nislk ut aliquip.</p><span class="date">4:04PM - MAY, 2016</span></div>
</section>

<footer class="abs site-footer">
  <h3 class="abs foot-head" style="left:85px">QUICK LINKS</h3>
  <ul class="abs foot-links">
    <li class="arrow">Digital Marketing About</li>
    <li class="arrow">Quorvo Promoline Contact</li>
    <li class="arrow">Chatterlane Advertising</li>
    <li>Privacy Policy</li>
    <li class="arrow">Search Engine Optimisation (SEO)</li>
    <li>Terms &amp; Conditions</li>
    <li class="arrow">Website Hosting FAQ</li>
    <li class="arrow">Newsletter Management</li>
  </ul>

  <h3 class="abs foot-head" style="left:289px">CONTACT INFO</h3>
  <svg class="abs" style="left:289px;top:62px" width="10" height="14" viewBox="0 0 10 14"><path d="M5 0a5 5 0 0 1 5 5c0 3.5-5 9-5 9S0 8.5 0 5a5 5 0 0 1 5-5z" fill="#fff"/><circle cx="5" cy="5" r="2" fill="var(--footer)"/></svg>
  <div class="abs foot-contact" style="left:308px;top:61px"><strong>HALLMERE</strong><br>14 Marlow Close Bracknell<br>Berskhire ZZ9 4QT</div>
  <svg class="abs" style="left:288px;top:112px" width="10" height="10" viewBox="0 0 10 10"><path d="M2 0.5l2 2-1 1.2c.6 1.3 1.7 2.4 3 3l1.2-1 2 2-1.3 1.6C4 9 1 6 0.6 1.8z" fill="#fff"/></svg>
  <div class="abs foot-contact" style="left:307px;top:110px">01632 960481</div>
  <svg class="abs" style="left:288px;top:135px" width="11" height="9" viewBox="0 0 11 9"><rect x="0.5" y="0.5" width="10" height="8" fill="#fff"/><path d="M0.5 0.5l5 4 5-4" stroke="var(--footer)" fill="none"/></svg>
  <div class="abs foot-contact" style="left:309px;top:133px">info@brightcrest-demo.com</div>

  <div class="abs map-block" role="img" aria-label="Street map of the office location in Bracknell with a location pin"></div>
  <div class="abs view-map">View Map ⟶</div>
</footer>

<div class="abs bottom-bar">
  <span class="abs" style="left:88px;top:12px">Follow Us</span>
  <span class="abs social" style="left:134px" role="img" aria-label="Chatterlane"></span>
  <span class="abs social" style="left:161px" role="img" aria-label="Pipwave"></span>
  <span class="abs social" style="left:188px" role="img" aria-label="Careernest"></span>
  <span class="abs" style="right:86px;top:12px">Copyright © 2016 BrightCrest. All Rights Reserved</span>
</div>

</body>
</html>
```